Design Creative Banner or Gif Ads. 3 Designs To Be Selected

Come up with some creative banner ads for stonewell.co.nz

*At least 3 different winning banners will be chosen*

Please provide banner ads / gif ads in common google ads / website banner formats.

They can be gif or static but must stand out while still maintaining clear clean text and visuals, with a premium professional feel (please avoid clip art or anything that gives a cheap message).

Please keep in mind that these will likely be small ads so text needs to be large and if there's there a lot of text then use multiple frames/ pages as submit as a gif.

Style
Minimal & clean lines
Architectural or realistic images
Avoid cartoon styles, clipart, or anything that looks cheap

Font
Nexa or Montserrat or similar

Tone
Premium, serious, trustworthy — fits new builds

Colours
Option 1: Deep Navy (trust & quality) & lighter blues and warm grey
Option 2: Open to bright colours to help the ads stand out, such as (but not limited to) bright pink with black, yellow, fluorescent green, provided the messaging is still done professionally.
Our logo is attached (Stone Well Logo)

Display Sizes
Ad specs for file sizes should be file formats like JPEG, GIF, and PNG, with animations limited to a max of 30 seconds or less.
We will need several different ad sizes provided for each of the 3 selected winning designs.

• Medium Rectangle: 300 × 250 pixels
• Leaderboard: 728 × 90 pixels
• Desktop Banner ad image: (640x360 pixels)
• Desktop Banner ad image 2: (300x600 pixels)
• Possibly one or two other sizes

Flexibility to be creative
The ad text, words, upper/lower case, layout, colour, theme, and images can be adjusted to how you think it will look best. The follow example ads are just examples of what we are after but we are keen to see what you can create.

Recommendations at this point:
1. Avoid text heavy
2. Looking for more Gif ads
3. Imaging: if possible use real stock photo's rather than AI

Themes:

1
Building Soon? Start Here
Free Build Planning Pack:
✓ Build Cost Calculator
✓ Hidden Cost Checklist
✓ Builder Comparison Guide
Build With Confidence
Download Free

2
Before You Choose A Builder
Compare Price, Scope, Risk & Value
Avoid Costly Mistakes
Choose The Right Builder With Confidence
Download The Free Guide

3
Planning A New Build?
Avoid These Common Mistakes:
✗ Hidden Exclusions
✗ Missing Scope
✗ Unrealistic Allowances
✗ Budget Blowouts
Download The Free Guide

4
Before You Buy Land
Know what it could cost to build.
Avoid Costly Building Mistakes
Download Our Free Guides

5
Know Your Build Budget?
• Free Build Cost Calculator
• Hidden Cost Checklist
• Build Planning Tools
Calculate Costs (Download)

Target Market(s)

Landowners looking to build

Industry/Entity Type

Building

Font styles to use
Other font styles liked:
• Nexa or Montserrat or similar

Requirements
Should not have
• Avoid cartoon styles, clipart, or anything that looks cheap

```html
<!DOCTYPE html>
<html lang="en">
<head>
<meta charset="utf-8">
<title>Stone Well – Where Is Your Build Budget Going?</title>
<link rel="stylesheet" href="https://fonts.googleapis.com/css2?family=Montserrat:wght@400;500;600;700;800;900&display=swap">
<style>
  :root {
    --navy-deep: #0f1a2b;
    --navy-panel: #0f2f52;
    --blue-accent: #2f7fc1;
    --blue-button: #3281bd;
    --blue-light: #8fc4ec;
    --steel-light: #a9bccb;
    --white: #ffffff;
  }
  * { margin: 0; padding: 0; box-sizing: border-box; }
  html, body {
    width: 1200px; height: 1051px; overflow: hidden;
    background: var(--navy-deep);
    font-family: "Montserrat", sans-serif;
  }
  .banner {
    position: relative; width: 1200px; height: 1051px; overflow: hidden;
    background: var(--navy-deep);
  }
  .bucket-photo {
    position: absolute; left: 560px; top: 0; width: 640px; height: 1051px;
    background:
      radial-gradient(ellipse 48% 50% at 68% 50%, #9a9fa4 0%, #6c737a 45%, rgba(40,48,58,0.6) 75%, rgba(15,26,43,0) 100%),
      linear-gradient(90deg, var(--navy-deep) 0%, #1a2535 40%, #232d3a 100%);
  }
  .brand { position: absolute; left: 79px; top: 110px; display: flex; align-items: center; gap: 34px; }
  .brand-square { width: 118px; height: 100px; background: var(--white); }
  .brand-name {
    font-size: 60px; font-weight: 600; color: var(--white); line-height: 1; letter-spacing: -0.5px;
  }
  .brand-tagline {
    margin-top: 14px; font-size: 15px; font-weight: 700; color: var(--blue-light); letter-spacing: 0.2px;
  }
  .headline {
    position: absolute; left: 80px; top: 295px;
    font-size: 69px; font-weight: 700; line-height: 87px; color: var(--white); letter-spacing: 1.5px;
  }
  .headline .accent { color: var(--blue-accent); font-weight: 900; letter-spacing: 0.5px; }
  .intro {
    position: absolute; left: 80px; top: 580px;
    font-size: 39px; font-weight: 400; line-height: 60px; color: var(--white);
  }
  .cta {
    position: absolute; left: 79px; top: 820px; width: 519px; height: 136px;
    background: var(--blue-button); display: flex; align-items: center; justify-content: space-between;
    padding: 0 36px;
    color: var(--white); font-size: 35px; font-weight: 700; line-height: 44px; letter-spacing: 1.5px;
    text-decoration: none;
  }
  .bucket-label {
    position: absolute; right: 23px; top: 176px; text-align: right;
    font-size: 68px; font-weight: 900; line-height: 60px; color: var(--steel-light); letter-spacing: -1px;
  }
  .cost-tag {
    position: absolute; left: 976px; width: 211px;
    background: var(--navy-panel); color: var(--white);
    font-size: 27px; font-weight: 700; line-height: 32px; letter-spacing: 0.8px;
    display: flex; align-items: center; padding-left: 14px;
  }
  .leaders { position: absolute; left: 0; top: 0; }
</style>
</head>
<body>
<div class="banner">
  <div class="bucket-photo" role="img" aria-label="Galvanised metal bucket with water pouring out of several holes onto a dark floor"></div>

  <div class="brand">
    <div class="brand-square"></div>
    <div>
      <div class="brand-name">Stone Well</div>
      <div class="brand-tagline">COMPARE QUOTES FROM TRUSTED BUILDERS</div>
    </div>
  </div>

  <h1 class="headline">WHERE IS YOUR<br><span class="accent">BUILD BUDGET</span><br>GOING?</h1>

  <p class="intro">Most homeowners don't<br>discover these costs<br>until it's too late.</p>

  <a class="cta" href="#">
    <span>DOWNLOAD OUR<br>FREE BUILD GUIDES</span>
    <svg width="26" height="40" viewBox="0 0 26 40" aria-hidden="true"><polyline points="5,5 20,20 5,35" fill="none" stroke="#ffffff" stroke-width="6"/></svg>
  </a>

  <div class="bucket-label">YOUR<br>BUILD<br>BUDGET</div>

  <svg class="leaders" width="1200" height="1051" aria-hidden="true">
    <g stroke="#ffffff" stroke-width="2">
      <line x1="823" y1="476" x2="976" y2="476"/>
      <line x1="786" y1="570" x2="976" y2="570"/>
      <line x1="856" y1="664" x2="976" y2="664"/>
      <line x1="828" y1="757" x2="976" y2="757"/>
      <line x1="804" y1="885" x2="976" y2="885"/>
    </g>
    <g fill="#ffffff">
      <circle cx="976" cy="476" r="4"/><circle cx="976" cy="570" r="4"/>
      <circle cx="976" cy="664" r="4"/><circle cx="976" cy="757" r="4"/>
      <circle cx="976" cy="885" r="4"/>
    </g>
  </svg>

  <div class="cost-tag" style="top:441px;height:64px;">Variations</div>
  <div class="cost-tag" style="top:535px;height:64px;">Site Costs</div>
  <div class="cost-tag" style="top:631px;height:64px;">PC Sums</div>
  <div class="cost-tag" style="top:724px;height:87px;">Provisional<br>Sums</div>
  <div class="cost-tag" style="top:857px;height:64px;">Delays</div>
</div>
</body>
</html>
```